Postcard Coupon Design

Local bar "The Mossy" we have great food, BBQ, wings, burgers, I would like to incorporate on the back company information such as happy hours, food specials,
and on the front a nice BBQ picture with some wings, and the following offers
"Free wings with any pitcher of regular priced beer"
"$5 off any check of $25 or more"
"Buy one get one free sandwiches 11am-3pm"
"Buy one get one free Appetizers"
The following on the back
"One coupon per customer per day, not to be combined with any other offers"
Check us out on Tapsheetly.com
www.themossy.com
happy hour 4-6pm M-F all beers and mixed drinks on special!
610-482-7319
218 Kelling Avenue
Ellbrook, KV 10482

Industry/Entity Type

It Company

Font styles to use
Serif
Sans Serif

Colors

Designer to choose colors to be used in the design.

```html
<!DOCTYPE html>
<html lang="en">
<head>
<meta charset="utf-8">
<title>The Mossy – Postcard Coupon</title>
<link href="https://fonts.googleapis.com/css2?family=Tinos:wght@400;700&display=swap" rel="stylesheet">
<style>
  :root {
    --paper: #ffffff;
    --card: #000000;
    --gold: #d9ae3f;
    --gold-light: #f1d27a;
    --gold-dark: #8a6418;
    --label: #000000;
  }
  * { margin: 0; padding: 0; box-sizing: border-box; }
  html, body { width: 776px; height: 1200px; overflow: hidden; background: var(--paper); }
  body { position: relative; font-family: "Tinos", "Times New Roman", serif; color: var(--gold); }
  .side-label { position: absolute; left: 0; width: 776px; text-align: center; color: var(--label); font-weight: 700; font-size: 46px; line-height: 1; }
  .card { position: absolute; left: 10px; width: 756px; height: 523px; background: var(--card); }
  .card--front { top: 69px; }
  .card--back { top: 667px; }
  .brand { position: absolute; left: 36px; top: 48px; width: 218px; height: 110px; display: flex; align-items: center; justify-content: center; gap: 10px; }
  .brand-dot { width: 14px; height: 14px; border-radius: 50%; background: var(--gold); }
  .brand-name { font-size: 40px; font-weight: 700; color: var(--gold); white-space: nowrap; }
  .contact { position: absolute; left: 0; width: 300px; text-align: center; font-size: 10px; line-height: 15px; color: var(--gold); white-space: nowrap; }
  .headline { position: absolute; text-align: center; line-height: 1; white-space: nowrap; }
  .coupons { position: absolute; left: 20px; top: 209px; width: 708px; height: 305px; border: 4px dashed var(--gold); }
  .coupons::before { content: ""; position: absolute; left: 348px; top: 0; bottom: 0; border-left: 4px dashed var(--gold); }
  .coupons::after { content: ""; position: absolute; left: 0; right: 0; top: 148px; border-top: 4px dashed var(--gold); }
  .offer { position: absolute; text-align: center; font-weight: 700; line-height: 1; white-space: nowrap; }
  .fine { position: absolute; font-size: 18px; line-height: 21px; white-space: nowrap; }
  .photo-frame { position: absolute; padding: 8px; background: linear-gradient(135deg, var(--gold-light), var(--gold) 40%, var(--gold-dark) 70%, var(--gold-light)); box-shadow: inset 0 0 0 2px var(--gold-dark); }
  .photo { width: 100%; height: 100%; box-shadow: 0 0 0 2px var(--gold-dark); }
  .photo--wings { background: radial-gradient(circle at 50% 50%, #6a3a1e, #3a1c0e 60%, #b01a12); }
  .photo--brisket { background: linear-gradient(135deg, #4a2314, #8c2a2a 45%, #c7655a 60%, #3a1a10); }
</style>
</head>
<body>
  <div class="side-label" style="top:16px;">front</div>

  <section class="card card--front">
    <div class="brand"><span class="brand-dot"></span><span class="brand-name">The Mossy</span></div>
    <div class="contact" style="top:160px;">610.482.7319, 218 Kelling Ave. ,Ellbrook, KV 10482<br>www.themossy.com</div>

    <div class="headline" style="left:232px; width:510px; top:19px; font-size:31px; font-weight:700;">Your Ardo Neighborhood Tavern</div>
    <div class="headline" style="left:232px; width:510px; top:53px; font-size:31px; font-weight:700;">for 60 years</div>
    <div class="headline" style="left:232px; width:500px; top:94px; font-size:19px; font-weight:700;">HAPPY HOUR</div>
    <div class="headline" style="left:232px; width:500px; top:116px; font-size:19px; font-weight:700;">4-6pm M-F</div>
    <div class="headline" style="left:232px; width:500px; top:137px; font-size:19px; font-weight:700;">ALL BEERS AND MIXED DRINKS ON SPECIAL</div>

    <div class="coupons"></div>

    <div class="photo-frame" style="left:40px; top:224px; width:122px; height:124px;">
      <div class="photo photo--wings" role="img" aria-label="Photo of barbecue chicken wings"></div>
    </div>
    <div class="offer" style="left:170px; width:186px; top:246px; font-size:31px;">FREE wings</div>
    <div class="offer" style="left:170px; width:186px; top:280px; font-size:17px;">with any pitcher</div>
    <div class="offer" style="left:170px; width:186px; top:299px; font-size:17px;">of regular priced beer</div>

    <div class="offer" style="left:384px; width:340px; top:249px; font-size:21px;">Buy one get one</div>
    <div class="offer" style="left:384px; width:340px; top:273px; font-size:31px;">FREE</div>
    <div class="offer" style="left:384px; width:340px; top:305px; font-size:21px;">Appetizers</div>

    <div class="offer" style="left:24px; width:344px; top:400px; font-size:17px;">Buy one get one</div>
    <div class="offer" style="left:24px; width:344px; top:418px; font-size:31px;">FREE SANDWICH</div>
    <div class="offer" style="left:24px; width:344px; top:454px; font-size:17px;">11am-3pm</div>

    <div class="offer" style="left:392px; width:160px; top:397px; font-size:42px;">$5 OFF</div>
    <div class="offer" style="left:392px; width:160px; top:442px; font-size:17px; line-height:17px;">any check of $25<br>or more</div>
    <div class="photo-frame" style="left:556px; top:383px; width:144px; height:88px;">
      <div class="photo photo--brisket" role="img" aria-label="Photo of sliced smoked barbecue brisket"></div>
    </div>
  </section>

  <div class="side-label" style="top:614px;">back</div>

  <section class="card card--back">
    <div class="brand"><span class="brand-dot"></span><span class="brand-name">The Mossy</span></div>
    <div class="contact" style="top:160px;">610.482.7319, 218 Kelling Ave. ,Ellbrook, KV 10482<br>www.themossy.com</div>

    <div class="headline" style="left:238px; width:500px; top:19px; font-size:31px;">Your Ardo Neighborhood Tavern</div>
    <div class="headline" style="left:238px; width:500px; top:53px; font-size:31px;">for 60 years</div>
    <div class="headline" style="left:280px; width:478px; top:147px; font-size:24px; font-weight:700;">Check us out on Tapsheetly.com</div>

    <div class="coupons"></div>

    <div class="fine" style="left:43px; top:264px;">One coupon per customer per day,<br>not to be combined with any other offers.</div>
    <div class="fine" style="left:405px; top:264px;">One coupon per customer per day,<br>not to be combined with any other offers.</div>
    <div class="fine" style="left:48px; top:411px;">One coupon per customer per day,<br>not to be combined with any other offers.</div>
    <div class="fine" style="left:404px; top:411px;">One coupon per customer per day,<br>not to be combined with any other offers.</div>
  </section>
</body>
</html>
```